To revamp the exting web page and Company presentation to new propsective client

We are company establish in 2006. We have a combine of Veltra implementation team of more than 10 years. We focus on the following areas

a) Veltra Nimbus suite implementation
b) Veltra Nimbus suite platform migration
c) Large database size in excess of 20TB

We need to redesign a our existing new card to give a new look and refresh look. Kindly visit our website for more info www.halvtek.com

Your main them is blue color and hope to hear from you all.

Target Market(s)

Professional clients

Industry/Entity Type

Information Technology

Contact Information for Business Card

To market our as the leading Veltra partner in Veltra nimbus suite implementation

Number of Pages Required

1 page

Colors
3276b5
9bcb3c
cadf82
33a6d7

Requirements
Must have
• The ability to attract new customer and show a level of professionalism.
• You can also add a green color to represent green and environmental friendly.
Nice to have
• To give a total new fresh look for the company
Should not have
• None

```html
<!DOCTYPE html>
<html lang="en">
<head>
<meta charset="utf-8">
<title>Halvtek Commerce Systems – Business Card</title>
<link rel="stylesheet" href="https://fonts.googleapis.com/css2?family=Open+Sans:wght@400;600;800&display=swap">
<style>
  :root {
    --stage: #2b2b2d;
    --brand-blue: #3276b5;
    --brand-sky: #33a6d7;
    --brand-green: #9bcb3c;
    --brand-lime: #cadf82;
    --card-light: #ffffff;
    --ink: #3a3a3c;
    --ink-soft: #5b5b5e;
    --on-blue: #ffffff;
  }
  * { box-sizing: border-box; margin: 0; padding: 0; }
  html, body {
    width: 1200px; height: 1000px; overflow: hidden;
    background: var(--stage);
    font-family: "Open Sans", Arial, sans-serif;
  }
  .stage { position: relative; width: 1200px; height: 1000px; }

  /* Front card */
  .card-front {
    position: absolute; left: 320px; top: 50px;
    width: 600px; height: 343px;
    background: var(--brand-blue);
    display: flex; align-items: center; justify-content: center;
  }
  .brand { display: flex; align-items: center; gap: 16px; }
  .brand-dot { width: 34px; height: 34px; border-radius: 50%; background: var(--brand-green); }
  .brand-text { display: flex; flex-direction: column; align-items: flex-end; }
  .brand-name {
    font-size: 44px; font-weight: 600; letter-spacing: 14px;
    color: var(--on-blue); line-height: 1;
  }
  .brand-sub {
    margin-top: 6px; font-size: 11px; font-weight: 600;
    letter-spacing: 3px; color: var(--brand-lime);
  }

  /* Back card */
  .card-back {
    position: absolute; left: 180px; top: 425px;
    width: 840px; height: 480px;
    background: var(--card-light);
  }
  .partner-badge {
    position: absolute; right: 70px; top: 60px;
    width: 90px; height: 28px; background: var(--brand-green);
  }
  .identity {
    position: absolute; left: 100px; top: 175px; text-align: right; width: 300px;
  }
  .person-name {
    font-size: 38px; font-weight: 800; color: var(--ink);
    letter-spacing: 1px; line-height: 1.05; white-space: nowrap;
  }
  .person-role { font-size: 17px; font-weight: 600; color: var(--brand-blue); letter-spacing: .3px; }
  .divider {
    position: absolute; left: 425px; top: 160px;
    width: 3px; height: 125px; background: var(--brand-sky);
  }
  .contacts {
    position: absolute; left: 445px; top: 158px; list-style: none;
  }
  .contacts li {
    display: flex; align-items: center; gap: 10px;
    font-size: 17px; color: var(--ink-soft); line-height: 21px; white-space: nowrap;
  }
  .contacts svg { width: 16px; height: 16px; fill: var(--brand-blue); flex: none; }
  .contacts svg.icon-globe { fill: none; stroke: var(--brand-blue); stroke-width: 1.4; }
  .contacts .tag, .contacts .web-strong { color: var(--brand-blue); }
  .address {
    position: absolute; left: 110px; top: 335px;
    display: flex; gap: 14px; font-size: 18px; font-style: normal;
    color: var(--ink-soft); line-height: 23px;
  }
  .address-label { color: var(--brand-green); font-size: 21px; white-space: nowrap; }
</style>
</head>
<body>
<main class="stage">
  <section class="card-front">
    <div class="brand">
      <span class="brand-dot"></span>
      <div class="brand-text">
        <span class="brand-name">HALVTEK</span>
        <span class="brand-sub">Commerce Systems Sdn Bhd</span>
      </div>
    </div>
  </section>

  <section class="card-back">
    <div class="partner-badge" aria-label="Partner badge"></div>

    <div class="identity">
      <h1 class="person-name">DORIAN VALE</h1>
      <p class="person-role">Chief Operating Officer</p>
    </div>

    <div class="divider"></div>

    <ul class="contacts">
      <li><svg viewBox="0 0 16 16"><path d="M4 1l2 3-1.5 1.5c.8 2 2.5 3.7 4.5 4.5L10.5 8.5l3 2-1 3C7 13 3 9 2.5 2z"/></svg><span>60 3 4418 7350</span></li>
      <li><svg viewBox="0 0 16 16"><path d="M4 1l2 3-1.5 1.5c.8 2 2.5 3.7 4.5 4.5L10.5 8.5l3 2-1 3C7 13 3 9 2.5 2z"/></svg><span>65 6271 0394 <span class="tag">(Singapore)</span></span></li>
      <li><svg viewBox="0 0 16 16"><path fill-rule="evenodd" d="M4 1h8v14H4zM5.5 2.5v10h5v-10z"/></svg><span>60 12 586 2143</span></li>
      <li><svg viewBox="0 0 16 16"><path fill-rule="evenodd" d="M4 1h7v4H4zM1 6h14v7h-3v2H4v-2H1zM5 10v4h6v-4z"/></svg><span>60 3 4418 7301</span></li>
      <li><svg viewBox="0 0 16 16"><path d="M1 3h14v10H1z"/><path d="M2 4l6 5 6-5" fill="none" stroke="#fff" stroke-width="1.2"/></svg><span>dorianvale@halvtek.com</span></li>
      <li><svg class="icon-globe" viewBox="0 0 16 16"><circle cx="8" cy="8" r="6.5"/><ellipse cx="8" cy="8" rx="2.8" ry="6.5"/><path d="M1.5 8h13"/></svg><span>www.<span class="web-strong">halvtek</span>.com</span></li>
    </ul>

    <address class="address">
      <span class="address-label">Address -</span>
      <span>Suite 6.04, 6th Floor, Menara Kestrel, Orchid Park,<br>Jalan Seri Lumina, 50480 Kuala Lumpur, Malaysia</span>
    </address>
  </section>
</main>
</body>
</html>
```